New brand for digital company - your chance to get creative

We need to create a brand for our new business 'Lanternfish Digital'. Please read the brief below before progressing as we are looking for some quite specific outputs.

Background

We are positioning ourselves as ‘marketing technologists’ - we're helping businesses engage with their customers in the online space.

Our tactics include branding, marketing, online management, and social media, however we are differentiating ourselves by focusing on overall strategy, not just tactics. Our tagline is ‘Online made simple’.

We have stipulated some parameters for the brand but otherwise want designers to exercise their creativity.

Requirements
Must have
• We want to see an entire concept, not just a logo.

```html
<!DOCTYPE html>
<html lang="en">
<head>
<meta charset="utf-8">
<title>Lanternfish Digital – Brand Concept</title>
<link rel="stylesheet" href="https://fonts.googleapis.com/css2?family=Exo:wght@300;400;600;700&display=swap">
<style>
  :root {
    --brand-pink: #d4236a;
    --canvas-grey: #e8e8e8;
    --paper: #ffffff;
    --ink: #1a1a1a;
    --photo-dark: #2b2b2b;
    --photo-mid: #6f6f6f;
    --photo-light: #b5b5b5;
  }
  * { box-sizing: border-box; margin: 0; padding: 0; }
  html, body { width: 1200px; height: 1000px; overflow: hidden; }
  body {
    position: relative;
    background: var(--canvas-grey);
    font-family: "Exo", Arial, sans-serif;
  }

  /* ---------- Flyer ---------- */
  .flyer {
    position: absolute; left: 50px; top: 42px; width: 688px; height: 918px;
    overflow: hidden; color: var(--paper);
  }
  .flyer__photo {
    position: absolute; inset: 0;
    background:
      radial-gradient(ellipse 45% 40% at 62% 45%, var(--photo-light), transparent 70%),
      linear-gradient(180deg, var(--photo-mid) 0%, #4a4a4a 45%, var(--photo-dark) 100%);
  }
  .flyer__shade {
    position: absolute; inset: 0;
    background: linear-gradient(90deg, rgba(0,0,0,.35) 0%, rgba(0,0,0,0) 60%);
  }
  .flyer__wordmark {
    position: absolute; left: 30px; top: 132px;
    font-size: 26px; font-weight: 400; letter-spacing: .2px;
  }
  .flyer__headline { position: absolute; left: 30px; top: 241px; }
  .headline-line {
    display: table; background: var(--brand-pink);
    font-size: 58px; line-height: 62px; padding: 0 14px 0 6px; margin-bottom: 16px;
  }
  .headline-line--light { font-weight: 300; }
  .headline-line--bold { font-weight: 700; }
  .flyer__intro {
    position: absolute; left: 30px; top: 608px; width: 410px;
    font-size: 18px; line-height: 22px; font-weight: 400;
  }
  .flyer__intro em { font-style: normal; color: var(--brand-pink); font-weight: 600; }
  .flyer__tagline { margin-top: 22px; }
  .flyer__rule {
    position: absolute; left: 30px; right: 30px; top: 816px;
    border-top: 2px dotted rgba(255,255,255,.8);
  }
  .flyer__details {
    position: absolute; top: 836px; font-size: 10px; line-height: 12.5px;
  }
  .flyer__details h4 { font-size: 10px; font-weight: 700; }
  .flyer__details--address { left: 30px; }
  .flyer__details--contact { left: 190px; }
  .flyer__footer-mark {
    position: absolute; right: 30px; top: 852px;
    font-size: 14px; font-weight: 400;
  }

  /* ---------- Type specimen sheet ---------- */
  .type-sheet {
    position: absolute; left: 590px; top: 64px; width: 566px; height: 424px;
    background: var(--paper); color: var(--ink);
  }
  .type-sheet__wordmark {
    position: absolute; left: 23px; top: 94px; font-size: 17px; font-weight: 400;
  }
  .type-sheet__rule {
    position: absolute; left: 23px; right: 23px; top: 131px;
    border-top: 1px dotted var(--brand-pink);
  }
  .spec-label { font-size: 11px; color: var(--brand-pink); font-weight: 600; }
  .spec-label span { color: var(--ink); font-weight: 400; }
  .type-sheet__headline-label { position: absolute; left: 23px; top: 156px; }
  .type-sheet__headline { position: absolute; left: 23px; top: 181px; }
  .headline-sample {
    display: table; background: var(--brand-pink); color: var(--paper);
    font-size: 34px; line-height: 40px; font-weight: 600; padding: 0 6px 0 2px; margin-bottom: 8px;
  }
  .spec-column { position: absolute; top: 337px; }
  .spec-column--sub { left: 23px; }
  .spec-column--body { left: 198px; }
  .spec-column--caption { left: 373px; }
  .spec-column .spec-label { margin-bottom: 8px; }
  .sample-sub { font-size: 10.5px; line-height: 12px; }
  .sample-sub b { font-weight: 600; }
  .sample-body { font-size: 6.5px; line-height: 7.5px; }
  .sample-caption { font-size: 4.5px; line-height: 5px; color: #555; }

  /* ---------- Brand card ---------- */
  .brand-card {
    position: absolute; left: 764px; top: 505px; width: 393px; height: 452px;
    background: var(--brand-pink); color: var(--paper);
    display: flex; align-items: center; justify-content: center; gap: 12px;
  }
  .brand-card__square { width: 30px; height: 30px; border: 2px solid var(--paper); }
  .brand-card__wordmark { font-size: 24px; font-weight: 600; }
</style>
</head>
<body>

  <section class="flyer">
    <div class="flyer__photo" role="img" aria-label="Black and white photograph of a smiling man in a plaid shirt seated on a tufted sofa in a studio"></div>
    <div class="flyer__shade"></div>

    <div class="flyer__wordmark">LanternfishDigital™</div>

    <h1 class="flyer__headline">
      <span class="headline-line headline-line--light">We Are</span>
      <span class="headline-line headline-line--bold">Lanternfish</span>
      <span class="headline-line headline-line--light">Digital</span>
    </h1>

    <div class="flyer__intro">
      <p>We secialise in <em>branding</em>, <em>marketing</em>, <em>online management</em>, and <em>social media</em>, however we differenciate ourselves by focusing on overall strategy, not just tactics.</p>
      <p class="flyer__tagline">We are...<em>online made simple</em></p>
    </div>

    <div class="flyer__rule"></div>

    <div class="flyer__details flyer__details--address">
      <h4>Address</h4>
      <p>1 Street Name</p>
      <p>Town, City</p>
      <p>Zip Code, Country</p>
    </div>
    <div class="flyer__details flyer__details--contact">
      <h4>Contact</h4>
      <p>+61 (02) 5550 0142</p>
      <p>www.lanternfishdigital.com</p>
      <p>info@lanternfishdigital.com</p>
    </div>

    <div class="flyer__footer-mark">Lanternfish</div>
  </section>

  <section class="type-sheet">
    <div class="type-sheet__wordmark">LanternfishDigital™</div>
    <div class="type-sheet__rule"></div>

    <p class="spec-label type-sheet__headline-label">Headline <span>(72 /84.4px)</span></p>
    <div class="type-sheet__headline">
      <span class="headline-sample">abcdefghijklmnopqrstuvwxy</span>
      <span class="headline-sample">ABCDEFGDEFGHIJKLIMN</span>
      <span class="headline-sample">0123456789!@£$</span>
    </div>

    <div class="spec-column spec-column--sub">
      <p class="spec-label">Subheader <span>(21 /24px)</span></p>
      <p class="sample-sub"><b>abcdefghijklmnopqrstuvwxyz</b><br>ABCDEFGHIJKVWXYZ<br>0123456789!@£$</p>
    </div>
    <div class="spec-column spec-column--body">
      <p class="spec-label">BodyCopy <span>(12 /15px)</span></p>
      <p class="sample-body"><b>abcdefghijklmnopqrstuvwxyz</b><br>ABCDEFGHIJKLMNOPQRSTUVWXYZ<br>0123456789!@£$</p>
    </div>
    <div class="spec-column spec-column--caption">
      <p class="spec-label">Caption <span>(8/9px)</span></p>
      <p class="sample-caption">abcdefghijklmnopqrstuvwxyz<br>ABCDEFGHIJKLMNOPQRSTUVWXYZ<br>0123456789!@£$</p>
    </div>
  </section>

  <section class="brand-card">
    <span class="brand-card__square"></span>
    <span class="brand-card__wordmark">LanternfishDigital™</span>
  </section>

</body>
</html>
```